Coaching Business Needs a Website

Business Name: Bright Orbit Coaching
My Name: Martin Hollowbrook

I am a human behaviour expert that needs not just a website, but in the process a "personality" for my brand (Bright Orbit).

With your brilliance and creativity, I want my reputation to be the go to expert in changing unresourceful human behaviour (eg. smoking, eating sugar, procrastination, overwhelm, fear, laziness, weight-gain, phobias, lack of motivation, etc).

===========================
Page 1 (Titled: 'Start Here')

My tag line is "Bright Orbit". The home page should be friendly, inviting, exciting, empowering, positive and innovative.

My Mission Quote: (so people know why I do what I do)

"Our mission is to improve as many people's lives as we can, when we can, through workshops, being guest speaker at events, coaching/mentoring and with valuable products." - Martin Hollowbrook, Human Behaviour Expert (I will give you a photo of me to put with this quote).

My marketing strategy is to share how I ride, because that is my focus (the experience that clients get). Please show the following on my Page 1:

- My mission quote (see above).
- A video (please insert any video at this stage, as I will get a marketing video professionally made to go on this page 1 of my website).
- 10 Reasons Why People Choose 'Bright Orbit Coaching'.
- What We Offer (with Call To Action Buttons, see below).
- Success Stories (these are our Testimonials).

-------------------------------------------
10 Reasons Why People Choose 'Bright Orbit Coaching':

Reason No. 1 We know how to make Bright Orbit in other people's lives. This is our favourite method of making change.

Reason No. 2 We give away a lot of FREE stuff.

Reason No. 3 We thank you for accepting FREE stuff. We are genuinely grateful for you accepting our FREE stuff.

Reason No. 4 We give you a feeling of belonging.

Reason No. 5 We give you the feeling that you are special, because you are.

Reason No. 6 We give you the feeling of significance, because you deserve it.

Reason No. 7 We give you the feeling of feeling good.

Reason No. 8 We give you positive, empowering experiences.

Reason No. 9 We give you tools, models and methodologies to improve every area of your life, continuously for the rest of your life. You can have fulfillment.

Reason No. 10 We give you value beyond what you can imagine.

What We Offer: (each of the following with a picture and more details)

1. Personal Coaching / Mentoring (more details: 1st Session FREE, valued at A$125, Unlimited chat support, call to action button to go to https://bookwell.example/brightorbitcoaching).

2. Human Behaviour Events (more details: next upcoming event, call to action button to go to... I will provide later.. I want to be able to change this hyperlink regularly to the latest upcoming event).

3. Guest Speaker / Master of Ceremonies (call to action button to go to 'Contact Us' website page).

4. Great Value Products (call to action button to go to 'Products' website page).

5. Great FREE Information (call to action button to go to 'Blogs' website page).

Success Stories:

Please allow for 10 written testimonial stories to be added. Please put 10 random text ones so I know what it will look like. I want to be able to change the text in the future. It would be good to put the person's picture and a star rating (eg. 5 stars).

Page 2 (Title: 'Products')

A place where I can add products...

Page 3 (Titled: 'Blogs')

A place where I can add written blogs...

Page 4 (Titled: 'Contact Us')

Contact us form with:
- Name
- Email Address
- Contact Number
- Message

Thank you. I look forward to working with you!!! I will upload my Logo for you to use.

Target Market(s)

Real, Everyday People - Men & Women aged between 21 - 50, who want to change several behaviours in their health, career, relationship, etc, that they feel are holding them back.

Industry/Entity Type

Life Coaching

Contact Information for Business Card

My Name: Martin Hollowbrook, Bright Orbit Expert
Mobile: xxxxxxxxxxxxxx
Email: xxxxxxxxxxxxxx@mailbox.example
Website: brightorbitcoaching.example.au

On the back have what we do:
1. Personal Coaching / Mentoring
2. Human Behaviour Events
3. Guest Speaker / Master of Ceremonies

Coding

Coded - Design and coding required

Number of Pages Required

4 page

Colors
ffc214

Requirements
Must have
• Inspiring images... My website must come across as fun, social, happy, and inviting. The website must have a personality; it is a marketing lead generation tool. It must represent Martin Hollowbrook as being a Human Behaviour Expert (ie. video & testimonials) and must have Call To Action buttons. The website should look professional, not something done using a cheap template. The colour selected is GOLD.
Nice to have
• Additional creative functionality...
Should not have
• It should not have anything negative on it.

```html
<!DOCTYPE html>
<html lang="en">
<head>
<meta charset="utf-8">
<title>Bright Orbit Coaching – Start Here</title>
<link href="https://fonts.googleapis.com/css2?family=Lato:wght@400;700;900&family=Open+Sans:ital,wght@0,400;0,600;0,700;1,400&family=Great+Vibes&display=swap" rel="stylesheet">
<style>
:root{
  --gold:#d4ad35;
  --gold-light:#f0cf5a;
  --gold-deep:#a8841c;
  --black:#050505;
  --ink:#111111;
  --charcoal:#2e2e2e;
  --slate:#3a3a3a;
  --white:#ffffff;
  --muted:#bdbdbd;
  --orange:#e8892a;
}
*{box-sizing:border-box;margin:0;padding:0}
html,body{width:1200px;height:4119px;overflow:hidden}
body{position:relative;background:var(--black);color:var(--white);font-family:"Open Sans",Arial,sans-serif;font-size:16px;line-height:1.55}
.abs{position:absolute}
.heading{font-family:"Lato",Arial,sans-serif;color:var(--gold-light);font-weight:400;letter-spacing:.5px}
.btn{position:absolute;display:flex;align-items:center;justify-content:center;background:linear-gradient(180deg,var(--gold-light),var(--gold-deep));color:var(--ink);font-family:"Lato",Arial,sans-serif;font-weight:700;letter-spacing:1px;text-decoration:none}

/* top bar */
.topbar{left:0;top:0;width:1200px;height:38px;background:var(--gold)}
.topbar .promo{left:86px;top:9px;font-size:12px;font-weight:700;letter-spacing:.5px}
.topbar .util{right:86px;top:9px;display:flex;gap:36px;font-size:12px;font-weight:700}
.util span{display:flex;align-items:center;gap:7px}

/* header */
.site-header{left:0;top:38px;width:1200px;height:149px;background:var(--black)}
.brand{left:82px;top:32px;display:flex;align-items:center;gap:16px}
.brand-mark{width:82px;height:82px;border-radius:50%;background:var(--gold)}
.brand-name{font-family:"Lato",Arial,sans-serif;font-weight:700;color:var(--gold-light);font-size:38px;line-height:1}
.brand-name small{display:block;font-size:19px;letter-spacing:8px;margin-top:6px}
.main-nav{right:86px;top:66px;display:flex;gap:30px;font-size:13px;font-weight:600;letter-spacing:.5px}
.main-nav span+span::before{content:"|";margin-right:30px;color:var(--white)}

/* hero */
.hero{left:0;top:187px;width:1200px;height:576px;background:radial-gradient(ellipse at 70% 40%,#5d5d5d,#333 55%,#1e1e1e)}
.hero-photo{left:0;top:0;width:600px;height:576px;background:linear-gradient(90deg,#2a3246 0%,#3c4968 45%,rgba(80,80,80,0) 100%)}
.hero-title{left:681px;top:148px;font-size:62px;font-weight:400;color:var(--gold-light);font-family:"Lato",Arial,sans-serif}
.hero-quote{left:686px;top:230px;width:440px;font-size:17px;font-style:italic;font-weight:600;line-height:1.45}
.hero-sign{left:870px;top:302px;font-family:"Great Vibes",cursive;font-size:32px;color:var(--gold-light)}
.hero-role{left:985px;top:345px;font-size:11px;color:var(--gold-light)}
.hero .btn{left:686px;top:384px;width:330px;height:49px;font-size:15px}

/* video */
.video-sec{left:0;top:763px;width:1200px;height:440px;background:var(--black)}
.video-sec h2{left:84px;top:67px;font-size:27px}
.video-copy{left:84px;top:110px;width:420px;font-size:16px;line-height:1.6}
.video-copy p+p{margin-top:22px}
.video-frame{left:593px;top:75px;width:525px;height:280px;background:linear-gradient(135deg,#1e2a4a,#3b4f7a 55%,#243050);border:1px solid #555}
.video-bar{left:0;bottom:0;width:100%;height:32px;background:rgba(0,0,0,.75)}

/* reasons */
.reasons{left:0;top:1203px;width:1200px;height:986px;background:var(--charcoal)}
.reasons h2{left:0;top:70px;width:1200px;text-align:center;font-size:33px;line-height:1.35}
.band{position:absolute;height:92px;background:linear-gradient(180deg,#555,#3c3c3c);border-top:2px solid #6a6a6a;border-bottom:2px solid #1b1b1b;display:flex;align-items:center;font-size:15px;line-height:1.5}
.band.left{left:0;width:434px;padding:0 110px 0 16px}
.band.right{left:758px;width:442px;padding:0 16px 0 110px;justify-content:flex-end;text-align:right}
.num{position:absolute;width:120px;height:120px;margin:-60px 0 0 -60px;border-radius:50%;background:#f4f4f4;box-shadow:0 3px 8px rgba(0,0,0,.6);display:flex;align-items:center;justify-content:center}
.num span{width:88px;height:88px;border-radius:50%;background:radial-gradient(circle at 40% 35%,var(--gold-light),var(--gold-deep));color:var(--ink);font-family:"Lato",Arial,sans-serif;font-size:40px;display:flex;align-items:center;justify-content:center}
.hub{left:475px;top:417px;width:248px;height:248px;border-radius:50%;background:#eee;display:flex;align-items:center;justify-content:center;box-shadow:0 4px 12px rgba(0,0,0,.7)}
.hub div{width:200px;height:200px;border-radius:50%;background:var(--black);border:6px solid var(--gold)}

/* offer */
.offer{left:0;top:2189px;width:1200px;height:1106px;background:var(--black)}
.offer h2{left:0;top:60px;width:1200px;text-align:center;font-size:32px}
.card{position:absolute;width:313px}
.card .pic{width:313px;height:213px}
.card h3{font-family:"Lato",Arial,sans-serif;font-weight:700;color:var(--gold-light);font-size:22px;line-height:1.2;margin-top:30px}
.card p{font-size:15px;margin-top:12px;line-height:1.55}
.card .btn{position:static;width:143px;height:36px;font-size:13px;margin-top:22px}

/* stories */
.stories{left:0;top:3295px;width:1200px;height:398px;background:var(--charcoal)}
.stories h2{left:0;top:66px;width:1200px;text-align:center;font-size:32px}
.story{position:absolute;top:147px;display:flex;gap:22px;width:520px}
.avatar{flex:none;width:102px;height:102px;border-radius:50%;margin-top:20px;background:radial-gradient(circle at 50% 40%,#c8a58a,#7c6b5d);border:3px solid #ddd}
.stars{color:var(--gold-light);font-size:17px;letter-spacing:1px}
.story p{font-size:14px;font-style:italic;color:var(--muted);line-height:1.6;margin-top:10px}
.story .who{color:var(--orange);font-size:14px;font-weight:600;margin-top:14px}
.pager{left:563px;top:308px;display:flex;gap:10px}
.pager span{width:32px;height:32px;border-radius:50%;background:#ddd;display:flex;align-items:center;justify-content:center}

/* footer */
.site-footer{left:0;top:3693px;width:1200px;height:366px;background:var(--black)}
.site-footer h4{position:absolute;font-family:"Lato",Arial,sans-serif;font-weight:400;color:var(--gold-light);font-size:24px;top:62px}
.field{position:absolute;left:82px;width:258px;height:55px;background:var(--white);color:#555;font-size:14px;display:flex;align-items:center;gap:12px;padding-left:16px}
.message{position:absolute;left:357px;top:118px;width:266px;height:124px;background:var(--white);color:#555;font-size:14px;padding:10px 14px}
.send{position:absolute;left:357px;top:261px;width:266px;height:55px;border:2px solid var(--gold);color:var(--gold-light);display:flex;align-items:center;justify-content:center;font-size:15px;letter-spacing:1px}
.social{position:absolute;left:712px;top:118px;display:grid;grid-template-columns:44px 44px;gap:16px 16px}
.social span{width:44px;height:44px;border-radius:50%;background:var(--gold)}
.contact{position:absolute;left:906px;top:106px;width:220px;font-size:14px}
.contact strong{display:block;font-size:15px;margin-bottom:18px}
.contact div{display:flex;gap:14px;margin-bottom:26px;line-height:1.6}
.contact svg{flex:none;margin-top:3px}
.bottombar{left:0;top:4059px;width:1200px;height:60px;background:var(--gold)}
.bottombar p{position:absolute;left:86px;top:20px;font-size:13px;color:var(--ink)}
.to-top{position:absolute;left:1075px;top:10px;width:40px;height:40px;border-radius:50%;background:#444;display:flex;align-items:center;justify-content:center}
</style>
</head>
<body>

<div class="abs topbar">
  <div class="abs promo">FREE SHIPPING &amp; FREE RETURNS</div>
  <div class="abs util">
    <span><svg width="14" height="14" viewBox="0 0 14 14"><circle cx="6" cy="6" r="4.5" fill="none" stroke="#fff" stroke-width="1.8"/><line x1="9.3" y1="9.3" x2="13" y2="13" stroke="#fff" stroke-width="1.8"/></svg>ACCOUNT</span>
    <span>MY CART</span>
    <span><svg width="16" height="14" viewBox="0 0 16 14"><path d="M1 1h3l2 8h8l1.5-6H5" fill="none" stroke="#fff" stroke-width="1.6"/><circle cx="7" cy="12" r="1.4" fill="#fff"/><circle cx="13" cy="12" r="1.4" fill="#fff"/></svg>$0.00</span>
  </div>
</div>

<header class="abs site-header">
  <div class="abs brand">
    <div class="brand-mark"></div>
    <div class="brand-name">Bright Orbit<small>COACHING</small></div>
  </div>
  <nav class="abs main-nav"><span>HOME</span><span>PRODUCTS</span><span>BLOGS</span><span>CONTACT US</span></nav>
</header>

<section class="abs hero">
  <div class="abs hero-photo" role="img" aria-label="Portrait photo of Martin Hollowbrook in a dark blue hoodie"></div>
  <h1 class="abs hero-title">BRIGHT ORBIT</h1>
  <p class="abs hero-quote">"Our mission is to improve as many people's lives as I can, when I can, through workshops, being guest speaker at events, coaching/mentoring and with valuable products."</p>
  <div class="abs hero-sign">- Martin Hollowbrook</div>
  <div class="abs hero-role">Bright Orbit Expert</div>
  <a class="btn" href="https://bookwell.example/brightorbitcoaching">BOOK APPOINTMENT - RIGHT NOW</a>
</section>

<section class="abs video-sec">
  <h2 class="abs heading">WATCH VIDEO</h2>
  <div class="abs video-copy">
    <p>Lorem Ipsum is simply dummy text of the printing and typesetting industry. Lorem Ipsum has been the industry's standard dummy text ever since the 1500s, when an unknown printer took a galley of type and scrambled it to make a type specimen book.</p>
    <p>It has survived not only five centuries, but also the leap into electronic typesetting, remaining essentially unchanged.</p>
  </div>
  <div class="abs video-frame" role="img" aria-label="Video still of a business meeting scene">
    <svg class="abs" style="left:222px;top:100px" width="82" height="82" viewBox="0 0 82 82"><circle cx="41" cy="41" r="37" fill="none" stroke="#fff" stroke-width="5"/><path d="M32 24 L58 41 L32 58Z" fill="#fff"/></svg>
    <div class="abs video-bar">
      <svg class="abs" style="left:14px;top:10px" width="12" height="12" viewBox="0 0 12 12"><path d="M1 0 L11 6 L1 12Z" fill="#fff"/></svg>
      <div class="abs" style="left:44px;top:14px;width:400px;height:4px;background:#888"></div>
      <div class="abs" style="left:44px;top:14px;width:60px;height:4px;background:#fff"></div>
      <div class="abs" style="left:460px;top:12px;width:40px;height:8px;background:#aaa"></div>
    </div>
  </div>
</section>

<section class="abs reasons">
  <h2 class="abs heading">10 REASONS WHY PEOPLE CHOOSE<br>“BRIGHT ORBIT COACHING”</h2>

  <div class="band left" style="top:220px">We know how to make Bright Orbit in other people's lives. This is our favourite method of making change.</div>
  <div class="band left" style="top:357px">We give away a lot of FREE stuff.</div>
  <div class="band left" style="top:495px">We thank you for accepting FREE stuff. We are genuinely grateful for you accepting our FREE stuff.</div>
  <div class="band left" style="top:638px">We give you a feeling of belonging.</div>
  <div class="band left" style="top:778px">We give you the feeling that you are special, because you are.</div>

  <div class="band right" style="top:220px">We give you the feeling of significance, because you deserve it.</div>
  <div class="band right" style="top:357px">We give you the feeling of feeling good.</div>
  <div class="band right" style="top:495px">We give you positive, empowering experiences.</div>
  <div class="band right" style="top:638px">We give you tools, models and methodologies to improve every area of your life, continuously for the rest of your life. You can have fulfillment.</div>
  <div class="band right" style="top:778px">We give you value beyond what you can imagine.</div>

  <svg class="abs" style="left:0;top:0" width="1200" height="986" viewBox="0 0 1200 986">
    <g stroke="#d4ad35" stroke-width="3" stroke-dasharray="2 9" stroke-linecap="round">
      <line x1="434" y1="266" x2="599" y2="541"/><line x1="434" y1="403" x2="599" y2="541"/>
      <line x1="434" y1="541" x2="599" y2="541"/><line x1="434" y1="684" x2="599" y2="541"/>
      <line x1="434" y1="824" x2="599" y2="541"/><line x1="758" y1="266" x2="599" y2="541"/>
      <line x1="758" y1="403" x2="599" y2="541"/><line x1="758" y1="541" x2="599" y2="541"/>
      <line x1="758" y1="684" x2="599" y2="541"/><line x1="758" y1="824" x2="599" y2="541"/>
    </g>
  </svg>

  <div class="abs hub"><div></div></div>

  <div class="num" style="left:434px;top:266px"><span>1</span></div>
  <div class="num" style="left:434px;top:403px"><span>2</span></div>
  <div class="num" style="left:434px;top:541px"><span>3</span></div>
  <div class="num" style="left:434px;top:684px"><span>4</span></div>
  <div class="num" style="left:434px;top:824px"><span>5</span></div>
  <div class="num" style="left:758px;top:266px"><span>6</span></div>
  <div class="num" style="left:758px;top:403px"><span>7</span></div>
  <div class="num" style="left:758px;top:541px"><span>8</span></div>
  <div class="num" style="left:758px;top:684px"><span>9</span></div>
  <div class="num" style="left:758px;top:824px"><span>10</span></div>
</section>

<section class="abs offer">
  <h2 class="abs heading">WHAT WE OFFER</h2>
  <div class="card" style="left:82px;top:137px">
    <div class="pic" role="img" aria-label="Photo of wooden letter blocks spelling life coach" style="background:linear-gradient(160deg,#f2f2f2,#c8b49a)"></div>
    <h3>Personal Coaching /<br>Mentoring</h3>
    <p>1st Session FREE, valued at A$125, 24/7 chat support.</p>
    <a class="btn" href="https://bookwell.example/brightorbitcoaching">LEARN MORE</a>
  </div>
  <div class="card" style="left:442px;top:137px">
    <div class="pic" role="img" aria-label="Photo of people seated at a workshop event" style="background:linear-gradient(160deg,#dfe3ea,#6d7a8c)"></div>
    <h3>Human Behaviour Events</h3>
    <p>Lorem Ipsum is simply dummy text of the printing and typesetting industry.</p>
    <a class="btn">LEARN MORE</a>
  </div>
  <div class="card" style="left:802px;top:137px">
    <div class="pic" role="img" aria-label="Photo of a lectern on stage before an audience" style="background:linear-gradient(180deg,#8a7a5a,#c9a878 60%,#6a4a2a)"></div>
    <h3>Guest Speaker / Master of<br>Ceremonies</h3>
    <p>Lorem Ipsum is simply dummy text of the printing and typesetting industry.</p>
    <a class="btn">LEARN MORE</a>
  </div>
  <div class="card" style="left:255px;top:612px">
    <div class="pic" role="img" aria-label="Photo of a hand marking a five star rating" style="background:linear-gradient(160deg,#fbfbfb,#cfd6e0)"></div>
    <h3 style="margin-top:30px">Great Value Products</h3>
    <p style="margin-top:30px">Lorem Ipsum is simply dummy text of the printing and typesetting industry.</p>
    <a class="btn">LEARN MORE</a>
  </div>
  <div class="card" style="left:615px;top:612px">
    <div class="pic" role="img" aria-label="Photo of hands typing on a laptop at a desk" style="background:linear-gradient(160deg,#e9d6c8,#b07c64)"></div>
    <h3 style="margin-top:30px">Great FREE Information</h3>
    <p style="margin-top:30px">Lorem Ipsum is simply dummy text of the printing and typesetting industry.</p>
    <a class="btn">LEARN MORE</a>
  </div>
</section>

<section class="abs stories">
  <h2 class="abs heading">SUCCESS STORIES</h2>
  <div class="story" style="left:91px">
    <div class="avatar" role="img" aria-label="Client portrait"></div>
    <div>
      <div class="stars">★★★★★</div>
      <p>“Lorem Ipsum is simply dummy text of the printing and typesetting industry. Lorem Ipsum has been the industry's standard dummy text ever since the 1500s.”</p>
      <div class="who">~ Name Here</div>
    </div>
  </div>
  <div class="story" style="left:640px">
    <div class="avatar" role="img" aria-label="Client portrait"></div>
    <div>
      <div class="stars">★★★★★</div>
      <p>“Lorem Ipsum is simply dummy text of the printing and typesetting industry. Lorem Ipsum has been the industry's standard dummy text ever since the 1500s.”</p>
      <div class="who">~ Name Here</div>
    </div>
  </div>
  <div class="abs pager">
    <span><svg width="10" height="12" viewBox="0 0 10 12"><path d="M8 1 L2 6 L8 11" fill="none" stroke="#333" stroke-width="2.4"/></svg></span>
    <span><svg width="10" height="12" viewBox="0 0 10 12"><path d="M2 1 L8 6 L2 11" fill="none" stroke="#333" stroke-width="2.4"/></svg></span>
  </div>
</section>

<footer class="abs site-footer">
  <h4 style="left:84px">SEND US A MESSAGE</h4>
  <div class="field" style="top:118px"><svg width="14" height="14" viewBox="0 0 14 14"><circle cx="7" cy="4" r="3.2" fill="#333"/><path d="M1 14c0-4 3-6 6-6s6 2 6 6z" fill="#333"/></svg>Full Name</div>
  <div class="field" style="top:190px"><svg width="14" height="11" viewBox="0 0 14 11"><rect x="0.5" y="0.5" width="13" height="10" fill="#333"/><path d="M1 1 L7 6 L13 1" fill="none" stroke="#fff" stroke-width="1.2"/></svg>Email</div>
  <div class="field" style="top:261px"><svg width="13" height="13" viewBox="0 0 13 13"><path d="M2 0.5 L4.5 0.5 L5.5 3.5 L4 5 C5 7 6 8 8 9 L9.5 7.5 L12.5 8.5 L12.5 11 C12.5 12 11.5 12.5 10.5 12.5 C5 12 1 8 0.5 2.5 C0.5 1.5 1 0.5 2 0.5Z" fill="#333"/></svg>Phone Number</div>
  <div class="message">Message</div>
  <div class="send">SEND NOW</div>

  <h4 style="left:712px">FIND US</h4>
  <div class="social" role="img" aria-label="Social network links">
    <span></span><span></span><span></span><span></span>
  </div>

  <h4 style="left:906px">CONTACT US</h4>
  <div class="contact">
    <strong>MAIN ADDRESS</strong>
    <div><svg width="12" height="16" viewBox="0 0 12 16"><path d="M6 0.5C3 0.5 0.8 2.8 0.8 5.7 0.8 9.5 6 15.5 6 15.5S11.2 9.5 11.2 5.7C11.2 2.8 9 0.5 6 0.5Z" fill="#d4ad35"/><circle cx="6" cy="5.7" r="2" fill="#050505"/></svg><span>Lorem Ipsum is simply dummy text of the printing.</span></div>
    <div><svg width="14" height="14" viewBox="0 0 13 13"><path d="M2 0.5 L4.5 0.5 L5.5 3.5 L4 5 C5 7 6 8 8 9 L9.5 7.5 L12.5 8.5 L12.5 11 C12.5 12 11.5 12.5 10.5 12.5 C5 12 1 8 0.5 2.5 C0.5 1.5 1 0.5 2 0.5Z" fill="#d4ad35"/></svg><span>123-456-789</span></div>
    <div><svg width="14" height="11" viewBox="0 0 14 11"><rect x="0.5" y="0.5" width="13" height="10" fill="#d4ad35"/><path d="M1 1 L7 6 L13 1" fill="none" stroke="#050505" stroke-width="1.2"/></svg><span>hello@brightorbit.example</span></div>
  </div>
</footer>

<div class="abs bottombar">
  <p>Copyright © 2017 Bright Orbit - All rights reserved.</p>
  <div class="to-top"><svg width="14" height="10" viewBox="0 0 14 10"><path d="M1 8 L7 2 L13 8" fill="none" stroke="#fff" stroke-width="2.4"/></svg></div>
</div>

</body>
</html>
```